Dorian's Lawn Service needs a postcard design

I need a design to attract lawn cutting customers. I am a high school junior, focusing on my city and the neighboring city. I think it would be advantageous to let my potential clients know I am earning money for my college education. They should also know, I will be working side by side with my father, who operated his own lawn service for 20 years, so they can be assured of a quality result for their lawn. I will be using state of the art, commercial equipment.

A few things that are unique to my service are; my mower weighs half of what other commercial mowers do (a softer footprint), my mower does NOT throw clippings into mulch or flower beds, at an additional charge I offer bagging of the clippings and/or dog waste clean-up. I am thinking about a two-sided design. I would also like a cartoon style picture of myself riding my mower. If this is something you can create, I can send you a photo of myself and a photo of my mower. If not, I can get this drawing done separately, then send it to you, I would just need to know what kind of file you would need it in. I am not going to have a business name, I want to introduce myself as Dorian to keep it simple and personal. We can add a coupon to the postcard, offering one free cut with commitment to a full 26 week season. The name of my high school is Marlowe High.

The cartoon picture attached is our logo.

Target Market(s)

Homeowners that use a commercial lawn cutting service, homeowners that need a temporary service while they are on vacation

Industry/Entity Type

School

Colors
3176b5
9bcb3c

Requirements
Must have
• An appeal for people to want to help me earn money for my college education. A clear idea they will be getting top notch service. I definitely want a drawing of myself on my mower. Phone # 612-905-3817
• design must work with parcelvaro.com/routeflyermailing guidelines

```html
<!DOCTYPE html>
<html lang="en">
<head>
<meta charset="utf-8">
<title>Dorian Lawn Cutting Service – Postcard Front</title>
<link rel="stylesheet" href="https://fonts.googleapis.com/css2?family=Questrial&family=Roboto+Slab:wght@300;400&family=Open+Sans:ital,wght@1,800&family=Roboto+Condensed:wght@400&family=Noto+Serif:ital@1&display=swap">
<style>
  :root {
    --blue: #1a5f9e;
    --blue-deep: #184f86;
    --green: #2a9a3c;
    --green-dark: #1d7f33;
    --green-light: #6cc04a;
    --lime: #9bcb3c;
    --photo-top: #8fae74;
    --photo-bottom: #5a9436;
    --ink: #222222;
    --paper: #ffffff;
    --backdrop: #e6e6e6;
  }
  * { box-sizing: border-box; margin: 0; padding: 0; }
  html, body { width: 1200px; height: 982px; overflow: hidden; background: var(--backdrop); }

  .postcard {
    position: absolute; left: 0; top: 29px;
    width: 1200px; height: 924px;
    background: var(--paper);
    overflow: hidden;
  }

  .hero-photo {
    position: absolute; left: 0; top: 0; width: 767px; height: 500px;
    background: linear-gradient(180deg, var(--photo-top) 0%, var(--photo-bottom) 100%);
  }
  .greeting {
    position: absolute; left: 324px; top: 334px; width: 240px;
    font-family: "Noto Serif", serif; font-style: italic;
    font-size: 37px; line-height: 53px; color: #fff; text-align: center;
  }

  .school-banner {
    position: absolute; left: 0; top: 500px; width: 767px; height: 167px;
    background: linear-gradient(90deg, var(--green-dark) 0%, var(--green) 60%, var(--green-dark) 100%);
    color: #fff; text-align: center;
    font-family: "Questrial", sans-serif; font-weight: 700;
    padding-top: 12px;
  }
  .school-banner .school { font-size: 32px; line-height: 39px; }
  .school-banner .mission { font-size: 35px; line-height: 42px; margin-top: 10px; }

  .brand-mark {
    position: absolute; left: 802px; top: 48px;
    width: 72px; height: 72px; border-radius: 50%; background: var(--blue);
  }
  .brand-name {
    position: absolute; left: 884px; top: 40px;
    font-family: "Roboto Slab", serif; font-weight: 400;
    font-size: 80px; line-height: 90px; color: var(--blue);
  }
  .brand-tag {
    position: absolute; left: 900px; top: 124px;
    font-family: "Questrial", sans-serif;
    font-size: 23px; line-height: 28px; color: var(--green);
  }

  .services { position: absolute; left: 792px; top: 240px; width: 400px; }
  .services h2 {
    font-family: "Roboto Slab", serif; font-weight: 400;
    font-size: 28px; color: var(--blue); line-height: 40px;
    display: inline-block; padding-right: 2px;
    border-bottom: 4px solid var(--green);
  }
  .service-list { list-style: none; margin-top: 28px; }
  .service-list li {
    position: relative; padding-left: 21px;
    font-family: "Questrial", sans-serif; font-size: 22px; line-height: 29px;
    color: var(--ink); margin-bottom: 18px;
  }
  .service-list svg { position: absolute; left: 0; top: 7px; width: 15px; height: 15px; }

  .intro {
    position: absolute; left: 13px; top: 721px; width: 460px;
    font-family: "Roboto Slab", serif; font-weight: 300;
    font-size: 22px; line-height: 42px; color: var(--ink);
  }

  .call-pill {
    position: absolute; left: 475px; top: 722px; width: 288px; height: 114px;
    border-radius: 57px; background: var(--blue);
    box-shadow: 0 4px 8px rgba(0,0,0,0.25);
    color: #fff; text-align: center;
    font-family: "Roboto Condensed", sans-serif;
    padding-top: 16px;
  }
  .call-pill .label { font-size: 29px; line-height: 38px; }
  .call-pill .phone { font-size: 35px; line-height: 44px; }

  .season-offer {
    position: absolute; left: 791px; top: 683px; width: 403px; height: 167px;
    border: 2px dashed #b0b0b0;
    font-family: "Open Sans", sans-serif; font-style: italic; font-weight: 800;
    font-size: 35px; line-height: 45px; color: var(--blue-deep);
    text-align: center; padding-top: 14px;
  }
  .season-offer .free { color: var(--green); }

  .footer-line { position: absolute; left: 0; top: 883px; width: 1200px; height: 7px; background: var(--green-light); }
  .footer-bar {
    position: absolute; left: 0; top: 895px; width: 1200px; height: 29px;
    background: linear-gradient(90deg, var(--green-dark), var(--green) 50%, var(--green-dark));
  }
</style>
</head>
<body>
<main class="postcard">
  <div class="hero-photo" role="img" aria-label="Photo of a country house lawn with a cartoon illustration of Dorian riding his lawn mower"></div>
  <p class="greeting">Hi, All<br>I Am Dorian</p>

  <section class="school-banner">
    <p class="school">Marlowe High<br>School Junior Student</p>
    <p class="mission">Earning Money For My College Education</p>
  </section>

  <span class="brand-mark"></span>
  <div class="brand-name">Dorian</div>
  <div class="brand-tag">Lawn Cutting Service</div>

  <section class="services">
    <h2>Service I Provide</h2>
    <ul class="service-list">
      <li><svg viewBox="0 0 16 16"><circle cx="8" cy="8" r="6.5" fill="none" stroke="#2a9a3c" stroke-width="1.5"/><path d="M4.5 8.2l2.4 2.4 5-5.5" fill="none" stroke="#2a9a3c" stroke-width="2"/></svg>Assurnce of A Quality of Lawn<br>Cutting Service</li>
      <li><svg viewBox="0 0 16 16"><circle cx="8" cy="8" r="6.5" fill="none" stroke="#2a9a3c" stroke-width="1.5"/><path d="M4.5 8.2l2.4 2.4 5-5.5" fill="none" stroke="#2a9a3c" stroke-width="2"/></svg>My Mower Weighs Half Of What<br>Other Commercial Mowers Do</li>
      <li><svg viewBox="0 0 16 16"><circle cx="8" cy="8" r="6.5" fill="none" stroke="#2a9a3c" stroke-width="1.5"/><path d="M4.5 8.2l2.4 2.4 5-5.5" fill="none" stroke="#2a9a3c" stroke-width="2"/></svg>My Mower Does Not Throw<br>Clippings Into Mulch Or Flower<br>Beds</li>
      <li><svg viewBox="0 0 16 16"><circle cx="8" cy="8" r="6.5" fill="none" stroke="#2a9a3c" stroke-width="1.5"/><path d="M4.5 8.2l2.4 2.4 5-5.5" fill="none" stroke="#2a9a3c" stroke-width="2"/></svg>At An Additional Charge I Offer<br>Bagging of The Clippings And/<br>or Dog Waste Clean-up</li>
    </ul>
  </section>

  <p class="intro">I am Working Side By Side With My<br>Father, Who Operats His Own Lawn<br>Cutting Service For 20 Years</p>

  <div class="call-pill">
    <div class="label">Call Me Today</div>
    <div class="phone">612-905-3817</div>
  </div>

  <aside class="season-offer">
    Book Me for<br>26 Week Season&amp;<br>GET One Cut <span class="free">FREE</span>
  </aside>

  <div class="footer-line"></div>
  <div class="footer-bar"></div>
</main>
</body>
</html>
```